Business Card for Ferncliff Massage

I need a business card for my massage therapy & cannabis oil practice. I already have a logo,the "massage" got edited out of this file. I will send the original soon. I need these elements to be on the card:
web: FerncliffMassage.example
ph: 541/382-9147
email: Marla.Quintavelle@mailbox.example
Other slogans, statements to consider:
Science Geek, Massage Therapist, Neuromuscular Therapy, Cannabis Spa Treatments, Raindrop Therapy, Essential Oils
Target Market(s)
women between 20 & 65, people with enough $ to afford regular massage, people who recently had a motor vehicle accident, Halvora HMC insured
Industry/Entity Type
Massage Therapy
Contact Information for Business Card
I would like to see my bear logo featured; contact details, greens & blues preferred colors.

```html
<!DOCTYPE html>
<html lang="en">
<head>
<meta charset="utf-8">
<title>Ferncliff Massage – Business Card</title>
<link href="https://fonts.googleapis.com/css2?family=Lora:wght@400;700&display=swap" rel="stylesheet">
<style>
  :root {
    --page-bg: #d9d3cb;
    --card-light: #f4f2f1;
    --card-light-edge: #e9e4e3;
    --band-brown: #6e5148;
    --band-tan: #c9ab98;
    --panel-green: #1f5a2c;
    --panel-green-deep: #0f3d1a;
    --text-light: #eef1ec;
    --text-soft: #d6c7ba;
    --logo-green: #2f6a3a;
  }
  * { margin: 0; padding: 0; box-sizing: border-box; }
  html, body { width: 1200px; height: 970px; overflow: hidden; }
  body {
    background: var(--page-bg);
    font-family: "Lora", Georgia, serif;
    position: relative;
  }
  .business-card {
    position: absolute;
    left: 100px; top: 200px;
    width: 1000px; height: 570px;
    background: linear-gradient(160deg, var(--card-light) 0%, var(--card-light-edge) 100%);
    overflow: hidden;
    box-shadow: 0 10px 30px rgba(0,0,0,0.18);
  }
  .card-shapes { position: absolute; inset: 0; }
  .brand-block {
    position: absolute;
    left: 40px; top: 0;
    width: 420px; height: 570px;
    display: flex; flex-direction: column; align-items: center;
  }
  .brand-mark {
    margin-top: 170px;
    display: flex; align-items: center; gap: 18px;
  }
  .brand-dot {
    width: 46px; height: 46px; border-radius: 50%;
    background: var(--logo-green);
  }
  .brand-name {
    font-size: 74px; font-weight: 400;
    color: var(--logo-green);
    letter-spacing: -1px;
  }
  .brand-web {
    margin-top: 70px;
    font-size: 25px;
    color: var(--logo-green);
  }
  .contact-panel {
    position: absolute;
    left: 570px; top: 46px;
    width: 410px;
    color: var(--text-light);
  }
  .person-name { font-size: 32px; font-weight: 700; line-height: 1.05; }
  .person-role { font-size: 24px; color: var(--text-soft); }
  .address { margin-top: 26px; font-size: 23px; line-height: 1.35; }
  .contact-list { margin-top: 22px; list-style: none; font-size: 22px; }
  .contact-list li { display: flex; align-items: center; gap: 10px; line-height: 1.45; white-space: nowrap; }
  .contact-icon { width: 25px; height: 25px; flex: none; }
  .services-title { margin-top: 26px; font-size: 24px; font-weight: 700; color: var(--text-soft); letter-spacing: 0.5px; }
  .service-list { margin-top: 14px; list-style: none; font-size: 22px; color: var(--text-soft); }
  .service-list li { display: flex; align-items: center; gap: 12px; line-height: 1.45; white-space: nowrap; }
  .service-bullet { width: 16px; height: 16px; border-radius: 50%; background: var(--band-tan); flex: none; }
  .license { margin-top: 20px; font-size: 23px; color: var(--text-soft); }
</style>
</head>
<body>
  <div class="business-card">
    <svg class="card-shapes" width="1000" height="570" viewBox="0 0 1000 570" aria-hidden="true">
      <defs>
        <linearGradient id="panelGreen" x1="0" y1="0" x2="0" y2="1">
          <stop offset="0" stop-color="#235f30"/>
          <stop offset="1" stop-color="#0f3d1a"/>
        </linearGradient>
      </defs>
      <path d="M478 0 C520 80 500 200 500 290 C500 380 545 460 525 570 L1000 570 L1000 0 Z" fill="var(--band-tan)"/>
      <path d="M490 0 C532 80 512 200 512 290 C512 380 557 460 537 570 L1000 570 L1000 0 Z" fill="var(--band-brown)"/>
      <path d="M507 0 C549 80 529 200 529 290 C529 380 574 460 554 570 L1000 570 L1000 0 Z" fill="url(#panelGreen)"/>
    </svg>

    <div class="brand-block">
      <div class="brand-mark">
        <span class="brand-dot"></span>
        <span class="brand-name">Ferncliff</span>
      </div>
      <div class="brand-web">FerncliffMassage.example</div>
    </div>

    <div class="contact-panel">
      <div class="person-name">Marla Quintavelle</div>
      <div class="person-role">Massage Therapist</div>
      <div class="address">2870 NW Alder Ct<br>Bend, OR, 97701</div>
      <ul class="contact-list">
        <li>
          <svg class="contact-icon" viewBox="0 0 28 28" aria-hidden="true">
            <rect x="1" y="1" width="26" height="26" fill="var(--text-soft)"/>
            <path d="M9 6 L12 6 L13 11 L11 12.5 C12 15.5 13 16.8 15.5 18 L17 16 L22 17 L22 20.5 C22 21.5 21 22 20 22 C13 21.5 7 15 6.5 8.5 C6.5 7 7.5 6 9 6 Z" fill="var(--panel-green)"/>
          </svg>
          541-382-9147
        </li>
        <li>
          <svg class="contact-icon" viewBox="0 0 28 28" aria-hidden="true">
            <rect x="1" y="1" width="26" height="26" fill="var(--text-soft)"/>
            <rect x="5" y="8" width="18" height="13" fill="none" stroke="var(--panel-green)" stroke-width="2"/>
            <path d="M5 8 L14 15 L23 8 M5 21 L11.5 13.5 M23 21 L16.5 13.5" fill="none" stroke="var(--panel-green)" stroke-width="2"/>
          </svg>
          marla.quintavelle@mailbox.example
        </li>
      </ul>
      <div class="services-title">OUR SERVICES</div>
      <ul class="service-list">
        <li><span class="service-bullet"></span>Neuromuscular therapy</li>
        <li><span class="service-bullet"></span>"Verdant Calm" massage treatment</li>
        <li><span class="service-bullet"></span>Raindrop Therapy with Cannabis</li>
      </ul>
      <div class="license">LMT #5186</div>
    </div>
  </div>
</body>
</html>
```